Belmora Wines

Hi all,

My name’s Liam Dowsett and I run a small wine brand based in the Canberra Wine District, Australia. I’m currently in the process of branding the business and am looking for a designer to help develop a new visual direction.

Background
I’ll be growing my own fruit from a leased vineyard site Named 'Wrenhollow' and my family’s property named 'Tibbard Vale', with a stronger emphasis on organic practices and site expression.

The Direction
The brand will centre around single vineyard wines, with each wine reflecting the unique site it comes from. I’d like the branding to support this idea of place, origin, and authenticity.

In terms of visual style, I’m drawn to something that is:

Simple and effective
A balance between traditional and modern
Clean, considered, and not overly decorative

Nothing too over-the-top, the goal is something timeless that lets the wine and vineyard story speak for itself.

At this stage, I’m mainly looking for:

Conceptual design direction / ideas
Label design (with potential to expand into broader branding)

I’m open to creative interpretation, so if the story resonates with you, I’d love to see how you would approach it.

Below I've attached an example of the bottle shape I will be using.

Cheers,
Liam

Colors
0054AA
0677BA
7BADD7
CADEEF
E8F1F8
FFC000
F8CF3A
FAE287
FDF2CF
FEFAEE

Requirements
Must have
• Mix of modern and traditional

```html
<!DOCTYPE html>
<html lang="en">
<head>
<meta charset="utf-8">
<title>Belmora Vineyards – Tibbard Vale Riesling Label</title>
<link rel="stylesheet" href="https://fonts.googleapis.com/css2?family=Cormorant+Garamond:ital,wght@0,500;0,600;1,500;1,600&family=Mrs+Saint+Delafield&display=swap">
<style>
  :root {
    --canvas: #f6f6f4;
    --paper: #f0ede2;
    --ink: #3b3e46;
    --ink-soft: #6a6c72;
    --gold: #c9973f;
    --band: #2f3440;
    --heron-dark: #2b2620;
    --heron-gold: #9c7a45;
  }
  * { box-sizing: border-box; margin: 0; padding: 0; }
  html, body {
    width: 1200px; height: 1200px; overflow: hidden;
    background: var(--canvas);
  }
  .label {
    position: absolute; left: 201px; top: 60px;
    width: 797px; height: 1080px;
    background: var(--paper);
    font-family: "Cormorant Garamond", Georgia, serif;
    color: var(--ink);
  }
  .brand {
    position: absolute; top: 100px; left: 0; right: 0;
    display: flex; flex-direction: column; align-items: center;
  }
  .brand__name {
    font-size: 42px; font-weight: 600; letter-spacing: 4px; line-height: 1;
    padding: 0 6px 6px; border-bottom: 1.5px solid var(--ink);
  }
  .brand__sub {
    font-size: 18px; font-weight: 600; letter-spacing: 2px; margin-top: 4px;
  }
  .heron {
    position: absolute; left: 316px; top: 228px; width: 166px; height: 276px;
    background: linear-gradient(160deg, var(--heron-gold), var(--heron-dark));
    border-radius: 40% 40% 10% 10%;
    opacity: .85;
  }
  .heron__caption {
    position: absolute; top: 530px; left: 0; right: 0; text-align: center;
    font-style: italic; font-size: 18px; color: var(--ink-soft); letter-spacing: .5px;
  }
  .wine {
    position: absolute; top: 625px; left: 0; right: 0; height: 250px;
  }
  .wine__site {
    position: absolute; right: 384px; top: 50px; text-align: right; line-height: .95;
  }
  .wine__site-small { font-size: 46px; font-weight: 500; letter-spacing: 1.5px; display: block; }
  .wine__site-large { font-size: 74px; font-weight: 500; letter-spacing: 1px; display: block; }
  .wine__divider {
    position: absolute; left: 413px; top: 0; width: 1.5px; height: 250px; background: var(--ink);
  }
  .wine__details { position: absolute; left: 450px; top: 6px; }
  .wine__variety { font-style: italic; font-weight: 600; font-size: 44px; color: var(--gold); line-height: 1; }
  .wine__vintage { font-size: 40px; font-weight: 500; line-height: 1.2; margin-top: 8px; }
  .wine__spec { font-size: 19px; font-weight: 500; line-height: 1.35; margin-top: 14px; }
  .band {
    position: absolute; left: 0; bottom: 0; width: 797px; height: 190px;
  }
  .band svg { position: absolute; inset: 0; }
  .band__origin {
    position: absolute; left: 0; right: 0; top: 92px; text-align: center;
    font-family: "Mrs Saint Delafield", cursive;
    font-size: 52px; color: var(--gold); letter-spacing: 1px;
  }
</style>
</head>
<body>
  <div class="label">
    <div class="brand">
      <span class="brand__name">BELMORA</span>
      <span class="brand__sub">VINEYARDS</span>
    </div>

    <div class="heron" role="img" aria-label="Engraved illustration of a white-faced heron standing on a grass tuft"></div>
    <p class="heron__caption">White-faced Heron</p>

    <div class="wine">
      <div class="wine__site">
        <span class="wine__site-small">TIBBARD</span>
        <span class="wine__site-large">VALE</span>
      </div>
      <div class="wine__divider"></div>
      <div class="wine__details">
        <p class="wine__variety">Riesling</p>
        <p class="wine__vintage">2026</p>
        <p class="wine__spec">750 ml<br>12% Alc. Vol.</p>
      </div>
    </div>

    <div class="band">
      <svg width="797" height="190" viewBox="0 0 797 190" aria-hidden="true">
        <path fill="#2f3440" d="M0 14 L40 10 L80 16 L120 9 L160 13 L200 8 L240 14 L280 10 L320 15 L360 9 L400 13 L440 8 L480 14 L520 10 L560 15 L600 9 L640 13 L680 8 L720 14 L760 10 L797 13 L797 190 L0 190 Z"/>
      </svg>
      <p class="band__origin">Wine of Canberra, Australia</p>
    </div>
  </div>
</body>
</html>
```